Double-sided half page marketing handout for professional association conference

We need a collatoral piece that will go into conference attendees' registration packets. Handout will be double-sided, half-letter-sized page. Working print area is 8.1" by 5.3" for each side. Can be laid out either vertically or horizontally.

One side of the piece will be focused on my firm's contact information and broad scope of services:

Contact Information:
Halvoren Partners LLC
Local Government Consultants
555-314-2087
www.halvorenpartners.example
info@halvorenpartners.example

Services:
Bond Rating Assessments
Economic Development Consulting
Executive Dashboards
Public Policy Analysis
Governance Training & Support
Strategic Planning & Performance Management

The other side of the piece will focus on the Bond Rating Assessments (see http://www.halvorenpartners.example/Pages/Bond-Rating-Assessments.aspx and attachments for more detail). This side should contain the text:

"Considering issuing debt? Bond ratings make a difference. Did you know that on an average $20 million GO debt issuance a one rating-level difference can easily equate to over $350,000 in interest cost-savings under normal market conditions?

The ratings agencies use a combined quantitative and qualitative approach to arrive at your bond rating. Our Bond Ratings Assessment shows you precisely what the agencies are looking at, provides advice as to how to frame the conversation during ratings calls, and identifies both strategic opportunities to provide upgrade pressure and specific threats that may lead to a downgrade. Call or email us to find out more or to get an example assessment."

Go to www.halvorenpartners.example and see attached files for logo and a recent winning ArtFolio 1/4 page advertisement for style guidance.

Target Market(s)

Highly-educated, conservative local government executives.

Industry/Entity Type

Marketing

Font styles to use
Sans Serif

Colors
3277b5
85acd3
ffffff

Requirements
Must have
• Our logo, our contact information, basic information stated in Project Description. Feel free to modify language to make more clear or understandable.
Nice to have
• We rather not just a text piece - bringing in some graphical elements would be very nice.

```html
<!DOCTYPE html>
<html lang="en">
<head>
<meta charset="utf-8">
<title>Halvoren Partners LLC – Services Handout</title>
<link rel="stylesheet" href="https://fonts.googleapis.com/css2?family=Roboto+Condensed:ital,wght@0,400;0,700;1,700&display=swap">
<style>
  :root {
    --brand-blue: #3277b5;
    --brand-light: #85acd3;
    --brand-white: #ffffff;
    --ink: #111111;
    --paper: #ffffff;
    --photo-top: #dfe6ef;
    --photo-mid: #c9d6e6;
    --photo-low: #d8e2ee;
  }
  html, body {
    margin: 0;
    padding: 0;
    overflow: hidden;
    background: var(--paper);
  }
  .handout {
    position: relative;
    width: 1200px;
    height: 777px;
    overflow: hidden;
    background: var(--paper);
    font-family: "Roboto Condensed", "Arial Narrow", sans-serif;
  }
  .hero-photo {
    position: absolute;
    left: 33px;
    top: 30px;
    width: 818px;
    height: 575px;
    background: linear-gradient(160deg, var(--photo-top) 0%, #eef2f7 25%, var(--photo-mid) 60%, var(--photo-low) 100%);
  }
  .hero-photo::after {
    content: "";
    position: absolute;
    left: 0;
    right: 0;
    top: 135px;
    bottom: 0;
    background: rgba(255,255,255,0.35);
  }
  .hero-rule {
    position: absolute;
    left: 30px;
    top: 162px;
    width: 850px;
    height: 5px;
    background: var(--brand-blue);
  }
  .contact-band {
    position: absolute;
    left: 30px;
    top: 605px;
    width: 1138px;
    height: 140px;
    background: linear-gradient(180deg, #3f82be 0%, var(--brand-blue) 100%);
  }
  .edge-rule {
    position: absolute;
    left: 1196px;
    top: 40px;
    width: 2px;
    height: 705px;
    background: var(--brand-light);
  }
  .seal {
    position: absolute;
    left: 0;
    top: 0;
  }
  .services {
    position: absolute;
    left: 80px;
    top: 204px;
    margin: 0;
    padding: 0;
    list-style: none;
  }
  .services li {
    position: relative;
    padding-left: 28px;
    height: 66.5px;
    font-size: 27px;
    font-weight: 700;
    font-style: italic;
    color: var(--ink);
    letter-spacing: -0.2px;
  }
  .services li::before {
    content: "";
    position: absolute;
    left: 4px;
    top: 10px;
    width: 7px;
    height: 16px;
    background: var(--brand-blue);
    border-radius: 0 8px 8px 0;
  }
  .identity {
    position: absolute;
    left: 880px;
    top: 248px;
    width: 260px;
    text-align: center;
  }
  .identity .firm-name {
    margin: 0;
    font-size: 40px;
    line-height: 42px;
    font-weight: 400;
    color: var(--ink);
  }
  .identity .tagline {
    margin: 16px 0 0;
    font-size: 22px;
    line-height: 31px;
    color: var(--brand-white);
  }
  .call-to-action {
    position: absolute;
    left: 885px;
    top: 468px;
    width: 270px;
    margin: 0;
    text-align: center;
    font-size: 22px;
    line-height: 31px;
    font-weight: 700;
    color: var(--brand-white);
  }
  .contact-lines {
    position: absolute;
    left: 30px;
    top: 622px;
    width: 880px;
    text-align: center;
    color: var(--brand-white);
    font-size: 27px;
  }
  .contact-lines p {
    margin: 0;
    line-height: 48px;
  }
  .contact-lines svg {
    vertical-align: -3px;
  }
  .contact-lines .gap { display: inline-block; width: 10px; }
</style>
</head>
<body>
<main class="handout">
  <div class="hero-photo" role="img" aria-label="Close-up photograph of a hand holding a pen over financial figures beside a desk calculator, in pale blue tones"></div>
  <div class="hero-rule"></div>
  <div class="contact-band"></div>
  <div class="edge-rule"></div>

  <svg class="seal" width="1200" height="777" viewBox="0 0 1200 777" aria-hidden="true">
    <defs>
      <clipPath id="seal-clip"><rect x="0" y="0" width="1168" height="745"/></clipPath>
    </defs>
    <g clip-path="url(#seal-clip)">
      <circle cx="1150" cy="390" r="362" fill="var(--brand-light)" opacity="0.9"/>
      <circle cx="1150" cy="390" r="343" fill="var(--brand-blue)"/>
    </g>
  </svg>

  <ul class="services">
    <li>Bond Rating Assessments</li>
    <li>Economic Development Consulting</li>
    <li>Executive Dashboards</li>
    <li>Public Policy Analysis</li>
    <li>Governance Training &amp; Support</li>
    <li>Strategic Planning &amp; Performance Management</li>
  </ul>

  <div class="identity">
    <p class="firm-name">Halvoren Partners LLC</p>
    <p class="tagline">Local Government<br>Consultants</p>
  </div>

  <p class="call-to-action">Call or email us to find out more or to get an example assessment.</p>

  <div class="contact-lines">
    <p>
      <svg width="38" height="24" viewBox="0 0 38 24" aria-hidden="true">
        <path d="M2 9 Q19 -2 36 9 L33 13 L27 11 L27 8 Q19 5 11 8 L11 11 L5 13 Z" fill="#111"/>
        <path d="M9 14 L13 11 L25 11 L29 14 L31 23 L7 23 Z" fill="#111"/>
      </svg>
      555-314-2087<span class="gap"></span>
      <svg width="28" height="20" viewBox="0 0 28 20" aria-hidden="true">
        <rect x="1" y="1" width="26" height="18" fill="none" stroke="#111" stroke-width="2"/>
        <path d="M1 1 L14 11 L27 1 M1 19 L11 9 M27 19 L17 9" fill="none" stroke="#111" stroke-width="1.6"/>
      </svg>
      info@halvorenpartners.example
    </p>
    <p>Visit us at www.halvorenpartners.example to learn more.</p>
  </div>
</main>
</body>
</html>
```